Turfwisp.com needs a professional yet bold design to share our differences and convert customers!

We need web design for the only company to offer same day & next day lawn care services to the North Carolina Piedmont Triad area! Customers will be able to view cost and book their lawn service in 5 minutes via our website. We need to promote the following that set us apart: 1: No Contract 2: Instant Scheduling 3: Same Day Service 4: Fully Licensed and Insured, 5: Money Back Guarantee. We are the ONLY company in the area to offer this service.
The site needs to be bold to show the reasons we are different. "in your face", yet professional enough to earn a customer's trust. Inspiration can be drawn from sites such as broomsquadry.com, however the creative piece will be up to you to create a website that is perhaps unique, slightly tacky, different, etc. The key is for it to be the BEST in the area and easy to use without confusing customers. Must be able to allure customers in and have an easy checkout and booking procedure.
Updates

Reason: Request by some designers. Plan to make decision before this Friday.

Target Market(s)

People that want a simple, quick, and easy way to get someone to mow their grass!

Industry/Entity Type

It Company

Logo Text

Turf Wisp logo design opportunity to be offered as well.

Number of Pages Required

1 page

Requirements
Must have
• simple, bold, yet instill trust from the public.
Nice to have
• Need chat now, book now, popups showing % off that day. Need Zip code entry to price lawns. Need it to emphasize the quick process, reliability of the company, etc.

```html
<!DOCTYPE html>
<html lang="en">
<head>
<meta charset="utf-8">
<title>Turf Wisp – Same Day &amp; Next Day Lawn Care</title>
<link href="https://fonts.googleapis.com/css2?family=Antonio:wght@300;400;600;700&family=Arimo:wght@400;700&display=swap" rel="stylesheet">
<style>
:root{
  --charcoal:#3f4446;
  --green:#178f12;
  --green-dark:#0f7a0b;
  --green-light:#2aa31f;
  --orange:#f47a0a;
  --yellow:#f2e21a;
  --ink:#414750;
  --body:#555a60;
  --rule:#9a9ea3;
  --muted:#aeb2b5;
  --white:#ffffff;
}
*{box-sizing:border-box;margin:0;padding:0}
html,body{width:1124px;height:1200px;overflow:hidden;background:var(--white)}
body{position:relative;font-family:"Arimo",Arial,sans-serif;color:var(--body)}
.display{font-family:"Antonio",sans-serif;text-transform:uppercase;white-space:nowrap}

.site-header{position:absolute;top:0;left:0;width:1124px;height:59px;background:var(--charcoal)}
.brand{position:absolute;left:160px;top:6px;font-family:"Antonio",sans-serif;font-weight:700;font-size:42px;line-height:46px;color:var(--white)}
.main-nav{position:absolute;right:170px;top:13px;display:flex;font-family:"Antonio",sans-serif;font-weight:400;font-size:17px}
.main-nav a{display:block;height:46px;line-height:46px;padding:0 11px;color:var(--white);text-decoration:none}
.main-nav a.active{background:var(--green)}

.hero{position:absolute;top:59px;left:0;width:1124px;height:331px;background:radial-gradient(ellipse at 30% 40%,var(--green-light),var(--green) 60%,var(--green-dark))}
.worker-photo{position:absolute;left:177px;top:62px;width:225px;height:412px;background:linear-gradient(180deg,#4b5a4a,#2f5a36 45%,#274d2e 85%,#e4e6e4);border-radius:40px 40px 6px 6px;z-index:2}
.hero-copy{position:absolute;left:443px;top:112px;color:var(--white)}
.hero-copy .l1{font-weight:300;font-size:31px;line-height:37px}
.hero-copy .l2{font-weight:700;font-size:38px;line-height:42px}
.hero-copy .l3{font-weight:300;font-size:31px;line-height:38px}
.book-title{position:absolute;left:442px;top:258px;font-weight:300;font-size:26px;line-height:34px;color:var(--yellow)}
.zip-form{position:absolute;left:442px;top:298px;display:flex;height:41px;font-weight:300;font-size:26px}
.zip-form .field{width:136px;background:var(--white);color:var(--green);line-height:41px;text-align:center}
.zip-form .go{width:58px;background:var(--orange);color:var(--white);text-align:center;line-height:41px;font-weight:600}

.features{position:absolute;top:480px;left:161px;width:803px;display:flex;justify-content:space-between}
.feature{width:150px;text-align:center}
.feature svg{width:30px;height:30px;display:block;margin:0 auto 16px}
.feature h3{font-weight:600;font-size:18px;line-height:22px;color:var(--ink);margin-bottom:5px}
.feature p{font-size:10px;line-height:13px;width:128px;margin:0 auto}

.divider{position:absolute;top:666px;left:161px;width:803px;border-top:1px solid var(--rule)}

.testimonial-photo{position:absolute;left:210px;top:721px;width:180px;height:180px;border-radius:50%;border:3px solid #dcdcdc;background:radial-gradient(circle at 50% 40%,#e9e6e2 0,#d8d4cf 55%,#2a2c30 80%)}
.testimonial{position:absolute;left:423px;top:715px;width:505px}
.testimonial h2{font-weight:700;font-size:38px;line-height:44px;color:var(--ink);margin-bottom:18px}
.testimonial p{font-size:11px;line-height:13.4px;color:var(--body)}
.testimonial .author{margin-top:3px;font-weight:700;font-size:14px;color:var(--ink)}
.dots{display:flex;align-items:center;gap:7px;margin-top:16px}
.dots span{width:9px;height:9px;border-radius:50%;background:#7d828c}
.dots span.on{width:15px;height:15px;background:var(--ink)}

.cta-band{position:absolute;top:974px;left:0;width:1124px;height:161px;background:var(--green);text-align:center;color:var(--white)}
.cta-band h2{font-weight:600;font-size:15px;line-height:20px;margin-top:19px}
.cta-band p{font-weight:300;font-size:12px;line-height:14px;width:480px;margin:16px auto 0;white-space:normal}
.cta-band .btn{display:inline-block;margin-top:20px;background:var(--charcoal);padding:0 15px;height:30px;line-height:30px;font-weight:600;font-size:13px;color:var(--white);text-decoration:none}

.site-footer{position:absolute;top:1135px;left:0;width:1124px;height:65px;background:var(--charcoal)}
.footer-nav{position:absolute;left:161px;top:17px;display:flex;gap:8px;font-weight:600;font-size:12px}
.footer-nav a{color:var(--white);text-decoration:none}
.copyright{position:absolute;left:161px;top:42px;font-size:8px;color:var(--muted)}
.social{position:absolute;right:161px;top:12px;display:flex;gap:11px}
.social span{width:35px;height:35px;border-radius:50%;background:var(--green)}
</style>
</head>
<body>

<header class="site-header">
  <div class="brand">TURFWISP</div>
  <nav class="main-nav">
    <a class="active" href="#">HOME</a><a href="#">ABOUT</a><a href="#">SERVICES</a><a href="#">FAQS</a><a href="#">CONTACT US</a>
  </nav>
</header>

<section class="hero" aria-label="Hero"></section>

<div class="worker-photo" role="img" aria-label="Photo of a lawn care worker in green overalls holding a string trimmer"></div>

<div class="hero-copy display">
  <div class="l1">We are the only company to offer</div>
  <div class="l2">Same day &amp; next day lawn care services</div>
  <div class="l3">To the North Carolina Piedmont Triad area!</div>
</div>
<div class="book-title display">Book a lawn cleaning in 60 seconds</div>
<div class="zip-form display"><div class="field">Enter zip code</div><div class="go">GO</div></div>

<section class="features">
  <div class="feature">
    <svg viewBox="0 0 30 30" aria-hidden="true"><rect x="7" y="3" width="15" height="21" fill="#4a5058"/><g stroke="#fff" stroke-width="1.3"><path d="M10 8h9M10 11h9M10 14h9M10 17h6"/></g><path d="M18 24l8-8 2 2-8 8-3 1z" fill="#4a5058"/></svg>
    <h3 class="display">No Contract</h3>
    <p>Lorem ipsum dolor sit amet consectetur adipiscing elit sed do eiusmod tempor incididunt ut labore et dolore.</p>
  </div>
  <div class="feature">
    <svg viewBox="0 0 30 30" aria-hidden="true"><circle cx="15" cy="15" r="13" fill="none" stroke="#4a5058" stroke-width="2.5"/><path d="M15 7v8l5 3" stroke="#4a5058" stroke-width="2.2" fill="none"/></svg>
    <h3 class="display">Instant Scheduling</h3>
    <p>Duis aute irue dolor in repmerit in voluptate velit esse cillum dolore eu fugiat nulla pariatur. Excepteur sint occaecat.</p>
  </div>
  <div class="feature">
    <svg viewBox="0 0 30 30" aria-hidden="true"><rect x="3" y="5" width="24" height="22" fill="none" stroke="#4a5058" stroke-width="2"/><rect x="3" y="5" width="24" height="5" fill="#4a5058"/><path d="M9 2v6M21 2v6" stroke="#4a5058" stroke-width="2"/><text x="15" y="24" text-anchor="middle" font-family="Arimo,sans-serif" font-weight="700" font-size="10" fill="#4a5058">25</text></svg>
    <h3 class="display">Same Day Service</h3>
    <p>Lorem ipsum dolor sit amet consectetur adipiscing elit sed do eiusmod tempor incididunt ut labore et dolore.</p>
  </div>
  <div class="feature">
    <svg viewBox="0 0 30 30" aria-hidden="true"><rect x="3" y="13" width="6" height="13" fill="#4a5058"/><path d="M10 13l5-9c2 0 3 1 2.5 4L16 12h9c1.5 0 2 1.5 1.5 3l-3 10c-.5 1-1 1-2 1H10z" fill="#4a5058"/></svg>
    <h3 class="display">Licensed and Insured</h3>
    <p>Duis aute irue dolor in repmerit in voluptate velit esse cillum dolore eu fugiat nulla pariatur. Excepteur sint occaecat.</p>
  </div>
  <div class="feature">
    <svg viewBox="0 0 30 30" aria-hidden="true"><path d="M8 9l12-6 3 6z" fill="#4a5058"/><rect x="3" y="9" width="24" height="18" rx="2" fill="#4a5058"/><rect x="19" y="15" width="8" height="6" fill="#fff"/><circle cx="22" cy="18" r="1.3" fill="#4a5058"/></svg>
    <h3 class="display">Money Back Guarantee</h3>
    <p>Lorem ipsum dolor sit amet consectetur adipiscing elit sed do eiusmod tempor incididunt ut labore et dolore.</p>
  </div>
</section>

<div class="divider"></div>

<div class="testimonial-photo" role="img" aria-label="Round portrait photo of a smiling client"></div>
<section class="testimonial">
  <h2 class="display">Happy Clients</h2>
  <p>Sed ut perspiciatis, unde omnis iste natus error sit voluptatem accusantium doloremque laudantium, totam rem aperiam eaque ipsa, quae ab illo inventore veritatis et quasi architecto beatae vitae dicta sunt, explicabo. Nemo enim ipsam voluptatem, quia voluptas sit, aspernatur aut odit aut fugit, sed quia consequuntur magni dolores eos, qui ratione voluptatem sequi nesciunt, neque porro quisquam est, qui dolorem ipsum, quia dolor sit amet consectetur.</p>
  <div class="author">Coach Daniel Ortiz Reyes</div>
  <div class="dots"><span class="on"></span><span></span><span></span><span></span></div>
</section>

<section class="cta-band display">
  <h2>If a high tech company offered cleaning services</h2>
  <p>We're changing the image of cleaning companies by offering a convenient, organic, and fair labor service that gives remarkable cleaning delivered with a fully seamless online experience.</p>
  <a class="btn" href="#">Try us and see what the fuss is about</a>
</section>

<footer class="site-footer">
  <nav class="footer-nav display">
    <a href="#">About us</a><a href="#">Privacy policy</a><a href="#">Terms &amp; conditions</a><a href="#">Affiliates</a><a href="#">Contact us</a><a href="#">Sitemap</a>
  </nav>
  <div class="copyright">Turf Wisp Inc. is a Meadowline Living company. Copyright 2015.</div>
  <div class="social" aria-label="Social links">
    <span></span><span></span><span></span><span></span><span></span>
  </div>
</footer>

</body>
</html>
```